LABEL FOR BOTTLE of Whiskey

We are launching a new Cinnamon and Walnut Whiskey called
Merrowen

The Alc. by Vol. will be 45% and Proof 90. The size bottle will be 750ml

Target Market(s)

This will be for whiskey drinkers who enjoy experimenting with flavored whiskeys

Requirements
Must have
• Because the whiskey contains both walnuts and cinnamon both derived from trees, we chose the name merrowen which describes the horticultural technique whereby tissues of plants are joined so as to continue their growth together as part of the tree.
Nice to have
• While subtle we would like for the design to have an element of nature, modern .. like a root, tree trunk with interwingled roots blending together, it can have a botanical illustration of botanical grafting (see examples)

or it could have a distinct beautiful combination of artsy leaves from the walnut tree leaves and leaves from the cinnamon tree together

```html
<!DOCTYPE html>
<html lang="en">
<head>
<meta charset="utf-8">
<title>Merrowen Cinnamon and Walnut Whiskey Label</title>
<link href="https://fonts.googleapis.com/css2?family=Sancreek&family=Smokum&family=Oswald:wght@500;600&display=swap" rel="stylesheet">
<style>
  :root {
    --backdrop: #170a06;
    --label-orange: #c3541f;
    --label-orange-deep: #a9441a;
    --ink: #2a1f2a;
    --gold: #f0c662;
    --gold-soft: #e7b64f;
  }
  html, body {
    margin: 0;
    width: 1200px;
    height: 900px;
    overflow: hidden;
    background: var(--backdrop);
  }
  .canvas {
    position: relative;
    width: 1200px;
    height: 900px;
  }
  .label {
    position: absolute;
    left: 338px;
    top: 50px;
    width: 524px;
    height: 800px;
    background: radial-gradient(ellipse at 50% 40%, var(--label-orange) 0%, var(--label-orange) 55%, var(--label-orange-deep) 100%);
    border-radius: 6px;
    overflow: hidden;
  }
  .label-frame {
    position: absolute;
    inset: 0;
  }
  .botanical-art {
    position: absolute;
    left: 161px;
    top: 67px;
    width: 202px;
    height: 263px;
    border-radius: 45% 45% 30% 30%;
    background: radial-gradient(ellipse at 50% 45%, rgba(42,31,42,0.55) 0%, rgba(42,31,42,0.25) 55%, rgba(42,31,42,0) 75%);
  }
  .brand-name {
    position: absolute;
    left: 0;
    right: 0;
    top: 300px;
    margin: 0;
    text-align: center;
    font-family: "Sancreek", serif;
    font-weight: 400;
    font-size: 92px;
    line-height: 1.4;
    letter-spacing: 1px;
    color: var(--gold);
  }
  .flavour {
    position: absolute;
    left: 40px;
    right: 40px;
    top: 520px;
    margin: 0;
    text-align: center;
    font-family: "Smokum", serif;
    font-weight: 400;
    font-size: 46px;
    line-height: 50px;
    letter-spacing: 0.5px;
    color: var(--gold-soft);
    text-transform: uppercase;
  }
  .strength {
    position: absolute;
    left: 0;
    right: 0;
    top: 660px;
    margin: 0;
    text-align: center;
    font-family: "Oswald", sans-serif;
    font-weight: 500;
    font-size: 15px;
    letter-spacing: 0.5px;
    color: var(--ink);
  }
  .volume {
    position: absolute;
    left: 0;
    right: 0;
    top: 688px;
    margin: 0;
    text-align: center;
    font-family: "Oswald", sans-serif;
    font-weight: 600;
    font-size: 24px;
    line-height: 34px;
    color: var(--ink);
  }
</style>
</head>
<body>
<main class="canvas">
  <section class="label">
    <svg class="label-frame" width="524" height="800" viewBox="0 0 524 800" aria-hidden="true">
      <rect x="12" y="12" width="500" height="776" rx="14" fill="none" stroke="var(--ink)" stroke-width="4" stroke-dasharray="3 3" opacity="0.75"/>
      <rect x="18" y="18" width="488" height="764" rx="12" fill="none" stroke="var(--ink)" stroke-width="1" opacity="0.7"/>
      <path d="M50 30 H474 Q480 50 496 54 V746 Q480 750 474 770 H50 Q44 750 28 746 V54 Q44 50 50 30 Z" fill="none" stroke="var(--ink)" stroke-width="2" opacity="0.85"/>
      <path d="M140 740 Q190 712 222 708 M384 740 Q334 712 302 708" fill="none" stroke="var(--ink)" stroke-width="1.5" opacity="0.8"/>
    </svg>
    <div class="botanical-art" role="img" aria-label="Line illustration of walnut and cinnamon leaves growing from intertwined roots"></div>
    <h1 class="brand-name">Merrowen</h1>
    <p class="flavour">Cinnamon and Walnut<br>Whiskey</p>
    <p class="strength">90 PROOF 45% ALC. BY VOL.</p>
    <p class="volume">750ML</p>
  </section>
</main>
</body>
</html>
```